Colorful Live Music Concert Poster for Paper Lanterns

Looking for a portrait oriented "poster" promoting the band's upcoming show at Marlow Lounge on Sunday, 3/22 at 8 pm, and social version (square format for Instagram). <br/><br/>Copy:<br/>Paper Lanterns<br/>with The Quiet Tides<br/><br/>Marlow Lounge <br/>Sunday, March 22<br/>8 pm<br/><br/>Poster must be consistent with band's overall branding seen on www.paperlanternsmusic.example and it's Spotify page at https://music.example.net/artist/7QwErTy2uIoPaSdFgHjKl?si=123abcDEFghiJKLmnoPQrs <br/><br/>BUT, we wouldn't mind taking in a slightly updated direction. A good example is the cover for our recent single Blue Hours, which is consistent in theme and color palette while updating the design and color at the same time. <br/><br/>The attached files include some band logo art as well as examples of posters done for prior shows. <br/><br/>The posters need not include photos of the band, but if you are so inclined, we've uploaded some selects as well.<br/><br/>Thank you. <br/><br/>Martin<br/>Paper Lanterns

```html
<!DOCTYPE html>
<html lang="en">
<head>
<meta charset="utf-8">
<title>Paper Lanterns – Poster Designs Preview</title>
<link href="https://fonts.googleapis.com/css2?family=Montserrat:ital,wght@0,800;1,400&family=Poiret+One&family=Josefin+Sans:wght@300;400;700&display=swap" rel="stylesheet">
<style>
  :root {
    --navy: #1c2a5a;
    --navy-light: #24346a;
    --mint: #b0dcd7;
    --orange: #fbb11c;
    --sheet: #ffffff;
  }
  * { box-sizing: border-box; margin: 0; padding: 0; }
  html, body { width: 911px; height: 1200px; overflow: hidden; background: var(--sheet); }
  .sheet { position: relative; width: 911px; height: 1200px; }

  .sheet-heading { position: absolute; left: 44px; top: 26px; display: flex; align-items: baseline; gap: 14px; color: var(--navy); }
  .sheet-heading__title { font: 800 54px/1 "Montserrat", sans-serif; letter-spacing: 0.5px; }
  .sheet-heading__sub { font: italic 400 25px/1 "Montserrat", sans-serif; }

  .design { position: absolute; overflow: hidden; background: var(--navy); width: 395px; }
  .design--poster { height: 610px; top: 110px; }
  .design--square { height: 394px; top: 755px; }
  .design--left { left: 42px; }
  .design--right { left: 473px; }

  .design__art { position: absolute; inset: 0; }

  .billing { position: absolute; left: 36px; top: 30px; }
  .billing__band { font: 400 33px/1.08 "Poiret One", sans-serif; color: var(--mint); letter-spacing: 2px; text-transform: uppercase; }
  .billing__band span { display: block; }
  .billing__band span:first-child { padding-left: 14px; }
  .billing__with { font: 300 17px/1 "Josefin Sans", sans-serif; color: var(--mint); margin-top: 6px; }
  .billing__support { display: flex; align-items: center; gap: 8px; margin: 10px 0 0 4px; font: 700 20px/1.05 "Josefin Sans", sans-serif; color: var(--orange); text-transform: uppercase; }
  .billing__dot { width: 12px; height: 12px; border-radius: 50%; background: var(--orange); flex: none; }

  .details { position: absolute; left: 33px; font: 300 17px/25px "Josefin Sans", sans-serif; color: var(--mint); }
  .details__date-badge { display: inline-flex; align-items: center; justify-content: center; width: 32px; height: 32px; margin-left: 4px; border-radius: 50%; background: var(--orange); color: var(--navy); font-size: 16px; line-height: 1; vertical-align: middle; }
  .design--poster .details { top: 242px; }
  .design--square .details { top: 224px; font-size: 14px; line-height: 23px; }
  .design--square .details__date-badge { width: 26px; height: 26px; font-size: 13px; }
  .design--square .billing { top: 30px; }
  .design--square .billing__band { font-size: 31px; }
</style>
</head>
<body>
<main class="sheet">
  <header class="sheet-heading">
    <h1 class="sheet-heading__title">PREVIEW</h1>
    <p class="sheet-heading__sub">2 Poster Designs</p>
  </header>

  <!-- Poster, geometric version -->
  <section class="design design--poster design--left">
    <svg class="design__art" width="395" height="610" viewBox="0 0 395 610">
      <defs>
        <linearGradient id="stepsPoster" x1="0" y1="1" x2="1" y2="0">
          <stop offset="0" stop-color="#b0dcd7"/><stop offset="0.5" stop-color="#c3d7b8"/><stop offset="1" stop-color="#b0dcd7"/>
        </linearGradient>
      </defs>
      <polygon role="img" aria-label="Isometric staircase of mint and orange bricks" points="0,580 395,188 395,610 0,610" fill="url(#stepsPoster)"/>
    </svg>
    <div class="billing">
      <h2 class="billing__band"><span>Paper</span><span>Lanterns</span></h2>
      <p class="billing__with">with</p>
      <p class="billing__support"><span class="billing__dot"></span>The Quiet<br>Tides</p>
    </div>
    <p class="details">Marlow Lounge<br>Sunday, March <span class="details__date-badge">22</span><br>8 pm</p>
  </section>

  <!-- Poster, band photo version -->
  <section class="design design--poster design--right">
    <svg class="design__art" width="395" height="610" viewBox="0 0 395 610">
      <defs>
        <linearGradient id="photoPoster" x1="0" y1="0" x2="0" y2="1">
          <stop offset="0" stop-color="#d9d6d0"/><stop offset="0.5" stop-color="#c9a88c"/><stop offset="1" stop-color="#5b6a5e"/>
        </linearGradient>
      </defs>
      <rect role="img" aria-label="Faint brick wall line pattern" x="172" y="0" width="223" height="222" fill="var(--navy-light)"/>
      <rect role="img" aria-label="Faint brick wall line pattern" x="8" y="400" width="170" height="210" fill="var(--navy-light)"/>
      <path d="M156 386 A225 225 0 0 1 395 328" fill="none" stroke="var(--mint)" stroke-width="1.5"/>
      <circle role="img" aria-label="Photo of the two band members standing outdoors at sunset" cx="270" cy="498" r="156" fill="url(#photoPoster)"/>
    </svg>
    <div class="billing">
      <h2 class="billing__band"><span>Paper</span><span>Lanterns</span></h2>
      <p class="billing__with">with</p>
      <p class="billing__support"><span class="billing__dot"></span>The Quiet<br>Tides</p>
    </div>
    <p class="details">Marlow Lounge<br>Sunday, March <span class="details__date-badge">22</span><br>8 pm</p>
  </section>

  <!-- Square, geometric version -->
  <section class="design design--square design--left">
    <svg class="design__art" width="395" height="394" viewBox="0 0 395 394">
      <defs>
        <linearGradient id="stepsSquare" x1="0" y1="1" x2="1" y2="0">
          <stop offset="0" stop-color="#b0dcd7"/><stop offset="0.5" stop-color="#c3d7b8"/><stop offset="1" stop-color="#b0dcd7"/>
        </linearGradient>
      </defs>
      <polygon role="img" aria-label="Isometric staircase of mint and orange bricks" points="122,394 395,122 395,394" fill="url(#stepsSquare)"/>
    </svg>
    <div class="billing">
      <h2 class="billing__band"><span>Paper</span><span>Lanterns</span></h2>
      <p class="billing__with">with</p>
      <p class="billing__support"><span class="billing__dot"></span>The Quiet<br>Tides</p>
    </div>
    <p class="details">Marlow Lounge<br>Sunday, March <span class="details__date-badge">22</span><br>8 pm</p>
  </section>

  <!-- Square, band photo version -->
  <section class="design design--square design--right">
    <svg class="design__art" width="395" height="394" viewBox="0 0 395 394">
      <defs>
        <linearGradient id="photoSquare" x1="0" y1="0" x2="0" y2="1">
          <stop offset="0" stop-color="#d9d6d0"/><stop offset="0.5" stop-color="#c9a88c"/><stop offset="1" stop-color="#5b6a5e"/>
        </linearGradient>
      </defs>
      <rect role="img" aria-label="Faint brick wall line pattern" x="190" y="0" width="205" height="140" fill="var(--navy-light)"/>
      <rect role="img" aria-label="Faint brick wall line pattern" x="60" y="310" width="120" height="84" fill="var(--navy-light)"/>
      <path d="M205 193 A150 150 0 0 1 395 176" fill="none" stroke="var(--mint)" stroke-width="1.5"/>
      <circle role="img" aria-label="Photo of the two band members standing outdoors at sunset" cx="302" cy="292" r="130" fill="url(#photoSquare)"/>
    </svg>
    <div class="billing">
      <h2 class="billing__band"><span>Paper</span><span>Lanterns</span></h2>
      <p class="billing__with">with</p>
      <p class="billing__support"><span class="billing__dot"></span>The Quiet<br>Tides</p>
    </div>
    <p class="details">Marlow Lounge<br>Sunday, March <span class="details__date-badge">22</span><br>8 pm</p>
  </section>
</main>
</body>
</html>
```